Release Therapy business card that deals with the release of negative issues

I need a business card for my business called MEADOWS (A gentle shore to rest when you drift) ... I'm a therapist that deals with people releasing negative issues, by applying therapies that incorporate, hypnosis, aromatherapy and listen therapy..I like the colour green and soft blues...My idea is for a hand releasing butterflies, and incorporating soft clouds....
Target Market(s)
All people, all ages
Industry/Entity Type
Business
Contact Information for Business Card
MEADOWS"A Gentle Shore To Rest When You Drift"Yvette R BrockingtonRelease Therapist0411 743 781email: easingpaths4everyone@fernmail.example
Requirements
Must have
- butterflies and soft clouds
Nice to have
- I like the decorative and script fonts for business name, and also my name
- Marlene T Ashcombe...

```html
<!DOCTYPE html>
<html lang="en">
<head>
<meta charset="utf-8">
<title>Meadows – Business Cards</title>
<link rel="stylesheet" href="https://fonts.googleapis.com/css2?family=Great+Vibes&family=Montserrat:wght@300;400&display=swap">
<style>
  :root {
    --backdrop: #e9eaec;
    --sky-light: #f4f9fb;
    --sky-soft: #cfe8f2;
    --sky-mid: #a9d6e8;
    --mint-wash: #dcefe6;
    --teal: #2fa3c0;
    --teal-deep: #1b7f99;
    --leaf: #8cc63f;
    --paper: #ffffff;
  }
  * { box-sizing: border-box; margin: 0; padding: 0; }
  html, body {
    width: 1200px; height: 848px; overflow: hidden;
    background: var(--backdrop);
  }
  .canvas { position: relative; width: 1200px; height: 848px; }

  .card {
    position: absolute;
    width: 540px; height: 340px;
    overflow: hidden;
    box-shadow: 0 6px 18px rgba(0,0,0,0.12);
    font-family: "Montserrat", sans-serif;
    font-weight: 300;
  }
  .card--front { left: 60px; top: 110px; }
  .card--back { left: 600px; top: 390px; }

  .card__wash {
    position: absolute; inset: 0;
    background:
      radial-gradient(ellipse 60% 45% at 20% 15%, var(--sky-mid) 0%, transparent 70%),
      radial-gradient(ellipse 55% 40% at 85% 10%, var(--sky-soft) 0%, transparent 70%),
      radial-gradient(ellipse 70% 50% at 70% 90%, var(--mint-wash) 0%, transparent 70%),
      linear-gradient(170deg, var(--sky-soft) 0%, var(--sky-light) 55%, var(--mint-wash) 100%);
  }

  .brand { position: absolute; display: flex; align-items: center; gap: 10px; }
  .brand__dot { border-radius: 50%; background: var(--leaf); flex: none; }
  .brand__name {
    font-family: "Great Vibes", cursive;
    color: var(--teal);
    font-weight: 400;
    line-height: 1;
  }
  .tagline { position: absolute; color: var(--teal-deep); font-weight: 400; white-space: nowrap; }

  /* front card */
  .card--front .brand { left: 34px; top: 28px; }
  .card--front .brand__dot { width: 16px; height: 16px; }
  .card--front .brand__name { font-size: 48px; }
  .card--front .tagline { left: 36px; top: 88px; font-size: 10px; }

  .holder { position: absolute; left: 36px; top: 150px; }
  .holder__name {
    font-family: "Great Vibes", cursive;
    font-size: 40px; color: var(--teal-deep); line-height: 1;
  }
  .holder__role { font-size: 17px; color: var(--leaf); margin-top: 4px; font-weight: 400; }

  .contact { position: absolute; left: 36px; top: 248px; color: var(--teal); font-size: 15px; line-height: 1.5; }

  /* back card */
  .services {
    position: absolute; left: 40px; top: 34px;
    font-family: "Great Vibes", cursive; font-size: 22px; color: var(--teal);
  }
  .card--back .brand { left: 120px; top: 66px; }
  .card--back .brand__dot { width: 22px; height: 22px; }
  .card--back .brand__name { font-size: 80px; }
  .card--back .tagline { left: 120px; top: 150px; font-size: 14px; }
  .appointment__label { position: absolute; left: 250px; top: 174px; font-size: 15px; color: var(--leaf); font-weight: 400; }
  .appointment__box {
    position: absolute; left: 150px; top: 198px; width: 366px; height: 118px;
    background: var(--paper); border: 1.5px solid var(--sky-mid);
  }
</style>
</head>
<body>
<main class="canvas">

  <section class="card card--front">
    <div class="card__wash" role="img" aria-label="Soft watercolour sky with pale blue and mint clouds"></div>
    <div class="brand">
      <span class="brand__dot"></span>
      <span class="brand__name">Meadows</span>
    </div>
    <p class="tagline">A Gentle Shore To Rest When You Drift</p>
    <div class="holder">
      <p class="holder__name">Marlene T Ashcombe</p>
      <p class="holder__role">Release Therapist</p>
    </div>
    <div class="contact">
      <p>0452 186 930</p>
      <p>easingpaths4everyone@fernmail.example</p>
    </div>
  </section>

  <section class="card card--back">
    <div class="card__wash" role="img" aria-label="Soft watercolour sky with pale blue and mint clouds"></div>
    <p class="services">Hypnotherapy - Aromatherapy - Listen Therapy</p>
    <div class="brand">
      <span class="brand__dot"></span>
      <span class="brand__name">Meadows</span>
    </div>
    <p class="tagline">A Gentle Shore To Rest When You Drift</p>
    <p class="appointment__label">Next Appointment</p>
    <div class="appointment__box"></div>
  </section>

</main>
</body>
</html>
```